" É uma pequena fábrica com injetoras plásticas, e a produção poderá ser a mais variada possível. Podemos, por exemplo, criar desde utensílios plásticos (cabide, potes, baldes), brinquedos e, até mesmo, peças para indústrias. Temos também a parte de reciclagem, onde tratamos o plástico desde o lixo até a produção destes itens. No meu ponto de vista deve ser algo genérico, que demonstre criação, inovação, transformação, visão de futuro. "

```html
<!DOCTYPE html>
<html lang="pt-BR">
<head>
<meta charset="UTF-8">
<title>Moldare – Cartão de visita</title>
<link rel="stylesheet" href="https://fonts.googleapis.com/css2?family=Montserrat:wght@400;500;600;700;800&display=swap">
<style>
  :root {
    --navy: #1d2c4e;
    --navy-deep: #172440;
    --navy-soft: #24365d;
    --orange: #e9731c;
    --white: #ffffff;
    --paper: #f7f7f7;
    --backdrop: #dcdcdc;
    --grey-text: #8a93a6;
  }
  * { box-sizing: border-box; margin: 0; padding: 0; }
  html, body { width: 1200px; height: 1200px; overflow: hidden; }
  body {
    background: var(--backdrop);
    font-family: "Montserrat", sans-serif;
    position: relative;
  }
  .card {
    position: absolute;
    left: 150px;
    width: 900px;
    height: 514px;
    border-radius: 30px;
    overflow: hidden;
  }
  /* Front */
  .card-front { top: 70px; background: var(--paper); }
  .front-rule {
    position: absolute; top: 0; left: 790px;
    width: 6px; height: 100%; background: var(--navy);
  }
  .front-accent {
    position: absolute; top: 330px; left: 808px;
    width: 6px; height: 46px; background: var(--orange);
  }
  .brand {
    position: absolute; left: 170px; top: 205px;
    display: flex; align-items: center; gap: 18px;
  }
  .brand-square { width: 34px; height: 34px; background: var(--orange); }
  .brand-name {
    font-weight: 800; font-size: 62px; letter-spacing: 2px;
    color: var(--navy); line-height: 1;
  }
  .brand-tagline {
    position: absolute; left: 222px; top: 278px;
    font-size: 15px; font-weight: 500; letter-spacing: 5px;
    color: var(--grey-text); text-transform: uppercase;
  }
  /* Back */
  .card-back { top: 620px; background: var(--navy); }
  .back-shapes { position: absolute; inset: 0; }
  .back-mark {
    position: absolute; left: 70px; top: 330px;
    display: flex; align-items: center; gap: 16px;
  }
  .back-mark-square { width: 30px; height: 30px; background: var(--orange); }
  .back-mark-name {
    font-weight: 800; font-size: 54px; letter-spacing: 2px;
    color: var(--white); line-height: 1;
  }
  .contact {
    position: absolute; right: 150px; top: 112px;
    text-align: right; color: var(--white);
  }
  .person-name { font-weight: 800; font-size: 32px; letter-spacing: 1px; }
  .person-role { font-weight: 500; font-size: 14px; letter-spacing: 3px; margin-top: 2px; }
  .contact-list { list-style: none; margin-top: 30px; }
  .contact-list li {
    font-size: 15px; font-weight: 500; letter-spacing: 0.5px;
    height: 35px; line-height: 35px;
  }
  .contact-list .address { line-height: 22px; height: auto; padding-top: 7px; }
  .icon-column {
    position: absolute; left: 808px; top: 208px;
    display: flex; flex-direction: column; gap: 11px; align-items: center;
  }
  .icon { width: 24px; height: 24px; display: block; }
</style>
</head>
<body>

  <section class="card card-front" aria-label="Frente do cartão">
    <div class="front-rule"></div>
    <div class="front-accent"></div>
    <div class="brand">
      <span class="brand-square"></span>
      <span class="brand-name">MOLDARE</span>
    </div>
    <p class="brand-tagline">Injeção Plástica</p>
  </section>

  <section class="card card-back" aria-label="Verso do cartão">
    <svg class="back-shapes" width="900" height="514" viewBox="0 0 900 514">
      <polygon points="0,0 330,0 0,330" fill="var(--navy-soft)"/>
      <polygon points="0,514 260,514 0,300" fill="var(--navy-deep)"/>
      <polygon points="330,0 560,0 420,514 260,514" fill="var(--navy-deep)" opacity="0.5"/>
      <polygon points="790,60 860,0 900,0 900,514 790,514" fill="var(--white)"/>
      <rect x="772" y="300" width="6" height="214" fill="var(--orange)"/>
      <rect x="870" y="0" width="6" height="120" fill="var(--orange)" transform="translate(-10,0)"/>
    </svg>

    <div class="back-mark">
      <span class="back-mark-square"></span>
      <span class="back-mark-name">MOLDARE</span>
    </div>

    <div class="contact">
      <p class="person-name">LOREM IPSUM</p>
      <p class="person-role">DIRETOR</p>
      <ul class="contact-list">
        <li>(XX) 8888-8888</li>
        <li>CONTATO@MOLDARE.COM.BR</li>
        <li>/ MOLDARE</li>
        <li>/ MOLDARE</li>
        <li class="address">AV. DAS INDÚSTRIAS, 412 CJ. 305 -<br>CENTRO</li>
      </ul>
    </div>

    <div class="icon-column">
      <svg class="icon" viewBox="0 0 24 24" aria-label="Telefone">
        <circle cx="12" cy="12" r="12" fill="var(--navy)"/>
        <path d="M8.5 6.5l2 2-1.2 1.6c.7 1.6 2 2.9 3.6 3.6l1.6-1.2 2 2-1.3 1.9c-4.3-.4-8.1-4.2-8.5-8.5z" fill="var(--white)"/>
      </svg>
      <svg class="icon" viewBox="0 0 24 24" aria-label="E-mail">
        <circle cx="12" cy="12" r="12" fill="var(--navy)"/>
        <rect x="6" y="8" width="12" height="8" fill="var(--white)"/>
        <path d="M6 8l6 5 6-5" fill="none" stroke="var(--navy)" stroke-width="1.2"/>
      </svg>
      <svg class="icon" viewBox="0 0 24 24" aria-label="Rede social">
        <circle cx="12" cy="12" r="12" fill="var(--navy)"/>
      </svg>
      <svg class="icon" viewBox="0 0 24 24" aria-label="Rede social">
        <circle cx="12" cy="12" r="12" fill="var(--navy)"/>
      </svg>
      <svg class="icon" viewBox="0 0 24 24" aria-label="Endereço">
        <circle cx="12" cy="12" r="12" fill="var(--navy)"/>
        <path d="M12 5.5a4 4 0 0 1 4 4c0 3-4 8-4 8s-4-5-4-8a4 4 0 0 1 4-4z" fill="var(--white)"/>
        <circle cx="12" cy="9.5" r="1.5" fill="var(--navy)"/>
      </svg>
    </div>
  </section>

</body>
</html>
```